Keystride Sport And Fitness- Rates

I am opening up a new Gym/Training Facility. The Name of my New gym is Keystride Sports And Fitness. I am wanting to design a card that captures Membership Pricing/Personal Training Pricing. I will Upload the Logo. My colors are Red/Black/Silver. I really want there pricing card to "POP". IT needs to be very Professional and Clean. I will be placing these cards on a 5'7 . I would like these item on the card:
Name of Company: Keystride Sports And Fitness
Address:
2817 Wexley Commerce Dr.
Suite 312 Chantilly, VA 20418
Phone #: 703-555-0186
website: www.keystridesnf.example
Membership Rates:
$99/Month
$49 Heroes Rate
Family Plan:
2 People $149
3 People $199
4 People $299
Personal Training Rates:
1 session $102
5 sessions $490
10 sessions $940
20 sessions $1,800
40 sessions $3,400
Please be creative

```html
<!DOCTYPE html>
<html lang="en">
<head>
<meta charset="utf-8">
<title>Keystride Sports And Fitness – Rates Card</title>
<link rel="stylesheet" href="https://fonts.googleapis.com/css2?family=Jost:ital,wght@0,400;0,500;0,600;1,400;1,500;1,700;1,800&family=Arimo:wght@400&display=swap">
<style>
  :root {
    --page-bg: #5a0000;
    --card-bg: #3a3a3c;
    --card-upper: #4a4a4c;
    --card-lower: #343436;
    --stripe-light: #6c6c6e;
    --stripe-dark: #545456;
    --brand-red: #6b0000;
    --brand-red-glass: rgba(120, 0, 0, 0.55);
    --accent-yellow: #f5d21b;
    --text-white: #ffffff;
    --photo-dark: #1f1f21;
    --photo-mid: #5b5b5f;
    --photo-light: #8a8a90;
  }
  html, body {
    margin: 0;
    padding: 0;
    width: 1200px;
    height: 2416px;
    overflow: hidden;
    background: var(--page-bg);
  }
  .canvas {
    width: 1200px;
    height: 2416px;
    display: flex;
    align-items: center;
    justify-content: center;
  }
  .rates-card {
    width: 1040px;
    height: 1558px;
    display: block;
    box-shadow: 0 20px 60px rgba(0,0,0,0.5);
  }
  .brand-name { font-family: "Jost", sans-serif; font-weight: 500; fill: var(--text-white); }
  .brand-tagline { font-family: "Jost", sans-serif; font-weight: 400; fill: var(--text-white); letter-spacing: 1.6px; }
  .headline { font-family: "Jost", sans-serif; font-style: italic; font-weight: 800; fill: var(--accent-yellow); }
  .subhead { font-family: "Jost", sans-serif; font-style: italic; font-weight: 500; fill: var(--accent-yellow); }
  .section-title { font-family: "Jost", sans-serif; font-weight: 600; fill: var(--text-white); letter-spacing: 0.6px; }
  .price-line { font-family: "Jost", sans-serif; font-style: italic; font-weight: 400; fill: var(--text-white); letter-spacing: 0.4px; }
  .website { font-family: "Arimo", sans-serif; fill: var(--accent-yellow); letter-spacing: 3px; }
  .contact-label { font-family: "Arimo", sans-serif; fill: var(--text-white); }
  .contact-value { font-family: "Arimo", sans-serif; fill: var(--accent-yellow); }
</style>
</head>
<body>
<main class="canvas">
  <svg class="rates-card" viewBox="0 0 594 890" xmlns="http://www.w3.org/2000/svg">
    <defs>
      <linearGradient id="gym-photo-tone" x1="0" y1="0" x2="1" y2="1">
        <stop offset="0" stop-color="var(--photo-mid)"/>
        <stop offset="0.45" stop-color="var(--photo-light)"/>
        <stop offset="1" stop-color="var(--photo-dark)"/>
      </linearGradient>
    </defs>

    <!-- card base -->
    <rect class="card-base" x="0" y="0" width="594" height="890" fill="var(--card-bg)"/>
    <polygon class="card-upper" points="0,0 594,0 594,97 0,247" fill="var(--card-upper)"/>
    <polygon class="card-lower" points="0,747 594,587 594,890 0,890" fill="var(--card-lower)"/>

    <!-- angled stripes -->
    <polygon class="stripe-top" points="0,230 594,80 594,97 0,247" fill="var(--stripe-light)"/>
    <polygon class="stripe-bottom" points="0,747 594,587 594,602 0,764" fill="var(--stripe-dark)"/>

    <!-- gym photo area -->
    <polygon class="gym-photo" role="img" aria-label="Blurred gym floor photo with dumbbells and weight machines"
             points="0,247 594,97 594,587 0,747" fill="url(#gym-photo-tone)"/>

    <!-- red brand band -->
    <polygon class="brand-band" points="30,0 297,0 297,172 30,239" fill="var(--brand-red)"/>
    <polygon class="brand-band-glass" points="30,239 297,172 30,742" fill="var(--brand-red-glass)"/>

    <!-- brand lockup -->
    <circle class="brand-dot" cx="62" cy="90" r="25" fill="var(--text-white)"/>
    <text class="brand-name" x="98" y="100" font-size="31">KEYSTRIDE</text>
    <text class="brand-tagline" x="100" y="116" font-size="11">SPORTS AND FITNESS</text>

    <!-- headline -->
    <text class="headline" x="561" y="257" font-size="46" text-anchor="end">SHAPE</text>
    <text class="subhead" x="556" y="278" font-size="17" text-anchor="end">&amp; BE HEALTY</text>

    <!-- membership -->
    <text class="section-title" x="38" y="299" font-size="21">MEMBERSHIP :</text>
    <text class="price-line" x="64" y="330" font-size="16">$ 99/MONTH</text>
    <text class="price-line" x="64" y="353" font-size="16">$ 49 HEROES RATE</text>

    <!-- family plan -->
    <text class="section-title" x="38" y="427" font-size="21">FAMILY PLAN :</text>
    <text class="price-line" x="64" y="453" font-size="16">2 PEOPLE $149</text>
    <text class="price-line" x="64" y="476" font-size="16">3 PEOPLE $199</text>
    <text class="price-line" x="64" y="499" font-size="16">4 PEOPLE $ 299</text>

    <!-- personal training -->
    <text class="section-title" x="575" y="425" font-size="21" text-anchor="end">PERSONAL TRAINING :</text>
    <text class="price-line" x="554" y="455" font-size="16" text-anchor="end">1 SESSION $102</text>
    <text class="price-line" x="554" y="479" font-size="16" text-anchor="end">5 SESSIONS $ 490</text>
    <text class="price-line" x="554" y="503" font-size="16" text-anchor="end">10 SESSIONS $ 940</text>
    <text class="price-line" x="554" y="527" font-size="16" text-anchor="end">20 SESSIONS $ 1,800</text>
    <text class="price-line" x="554" y="551" font-size="16" text-anchor="end">40 SESSIONS $ 3,400</text>

    <!-- website -->
    <text class="website" x="314" y="626" font-size="10" text-anchor="middle">WWW.KEYSTRIDESNF.EXAMPLE</text>

    <!-- contact -->
    <text class="contact-label" x="556" y="743" font-size="11" text-anchor="end">CALL US</text>
    <text class="contact-value" x="556" y="764" font-size="21" text-anchor="end">703-555-0186</text>
    <text class="contact-label" x="556" y="791" font-size="11" text-anchor="end">ADDRESS</text>
    <text class="contact-value" x="556" y="812" font-size="17" text-anchor="end">2817 WEXLEY COMMERCE DR.</text>
    <text class="contact-value" x="556" y="835" font-size="17" text-anchor="end">SUITE 312 CHANTILLY, VA 20418</text>
  </svg>
</main>
</body>
</html>
```